Real Estate agent needs flyer/folder to contain bio and overview of services

I'm including files of the layout of the small folder. The folder is 6 1/2 across and 9 1/2 inches long. It will have a front & back cover and then writing on the 2 inside pages.

I am sending a few files to incorporate into the flyer, 1 new logo to use and 2 files which are coloring ideas.

```html
<!DOCTYPE html>
<html lang="en">
<head>
<meta charset="utf-8">
<title>Carla Benedetti – Realtor Folder</title>
<link href="https://fonts.googleapis.com/css2?family=PT+Sans:ital,wght@0,400;0,700;1,400&family=PT+Serif:wght@400;700&display=swap" rel="stylesheet">
<style>
  :root{
    --navy:#233a80;
    --bright:#0a7fc6;
    --paper:#ffffff;
    --mist:#ececec;
    --backdrop:#e2e2e2;
    --logo-blue:#2d4fb0;
    --ink:#2b2b2b;
    --photo-portrait:#b9a88c;
    --photo-estate-a:#3a4f86;
    --photo-estate-b:#5a7fb8;
    --photo-entrance-a:#6d8a64;
    --photo-entrance-b:#7d9a74;
  }
  *{margin:0;padding:0;box-sizing:border-box}
  html,body{width:1200px;height:750px;overflow:hidden;background:var(--backdrop)}
  body{position:relative;font-family:"PT Sans",sans-serif}

  .spread{position:absolute;top:170px;width:560px;height:409px;background:var(--paper);box-shadow:0 10px 28px rgba(0,0,0,.18)}
  .spread--outer{left:20px}
  .spread--inner{left:620px}
  .spread__shapes{position:absolute;inset:0;width:560px;height:409px}
  .fold{position:absolute;left:280px;top:0;width:1px;height:409px;background:rgba(0,0,0,.08)}

  .serif{font-family:"PT Serif",serif}
  .block{position:absolute}
  .body-text{font-size:4.7px;line-height:1.55;color:#fff}
  .body-text p+p{margin-top:3px}
  .sig{font-style:italic;font-weight:700;margin-top:4px}

  /* outer spread */
  .testimonials__title{position:absolute;left:21px;top:22px;font-family:"PT Serif",serif;font-weight:700;font-size:6.6px;color:#fff}
  .testimonials__col1{left:21px;top:31px;width:72px}
  .testimonials__col2{left:101px;top:31px;width:76px}
  .testimonials__col2 .quote+.quote{margin-top:12px}

  .brokerage{position:absolute;left:21px;top:262px;display:flex;align-items:center;gap:5px}
  .brokerage__dot{width:18px;height:18px;border-radius:50%;background:var(--navy)}
  .brokerage__name{font-size:8px;font-weight:700;color:var(--navy)}

  .contact{position:absolute;left:21px;top:319px;width:140px;font-size:5.8px;line-height:1.45;color:var(--ink)}
  .contact__list{margin-top:4px}

  .cover-logo{position:absolute;left:380px;top:60px;display:flex;align-items:center;gap:6px}
  .cover-logo__mark{width:14px;height:14px;background:#c9c9cc}
  .cover-logo__name{font-family:"PT Serif",serif;font-size:17px;color:var(--logo-blue)}

  .tagline{position:absolute;left:304px;top:234px;font-family:"PT Serif",serif;font-size:11px;line-height:1.2;color:#fff}

  /* inner spread */
  .photo{position:absolute}
  .photo--portrait{left:41px;top:0;width:43px;height:47px;background:var(--photo-portrait)}
  .photo--estate{left:280px;top:7px;width:216px;height:142px;background:linear-gradient(180deg,var(--photo-estate-a),var(--photo-estate-b));clip-path:polygon(0 0,100% 0,100% 82%,0 100%)}
  .photo--entrance{left:156px;top:151px;width:124px;height:130px;background:linear-gradient(180deg,var(--photo-entrance-a),var(--photo-entrance-b));clip-path:polygon(0 9%,100% 0,100% 87%,0 100%)}

  .heading{font-family:"PT Serif",serif;color:#fff}
  .intro__title{left:41px;top:58px;font-size:9px;font-weight:400}
  .intro__body{left:41px;top:72px;width:196px}
  .tenet__title{left:41px;top:187px;font-size:7px;font-weight:700;line-height:1.15}
  .tenet__body{left:41px;top:207px;width:94px}
  .services__title{left:41px;top:302px;font-size:7px;font-weight:700;color:var(--navy)}
  .services__body{left:41px;top:313px;width:120px;color:var(--ink)}
  .selling__title{left:298px;top:165px;font-size:7px;font-weight:700}
  .selling__body{left:298px;top:176px;width:94px}
  .buying__title{left:399px;top:208px;font-size:7px;font-weight:700}
  .buying__body{left:399px;top:219px;width:97px}
</style>
</head>
<body>

<!-- Outer: back cover + front cover -->
<section class="spread spread--outer">
  <svg class="spread__shapes" viewBox="0 0 560 409" aria-hidden="true">
    <polygon points="0,196 280,354 280,409 0,409" fill="var(--mist)"/>
    <polygon points="0,0 152,0 560,228 560,409 377,409 0,196" fill="var(--navy)"/>
  </svg>
  <div class="fold"></div>

  <h2 class="testimonials__title">Testimonials:</h2>
  <div class="block body-text testimonials__col1">
    <p>During the home buying process, Carla becomes your trusted advisor, mentor and friend. Her knowledge of the industry, community and market are best in class. A true professional! Carla aligned her goals with my own and understood the motivation behind my purchase. Carla is unequivocally the reason why I was able to purchase my home in Laguna Niguel and provide my family with a world-class community. Without her guidance and experience, I would still be in the market attempting to navigate the ever-changing work of real estate.</p>
    <p class="sig">Dana Whitfield</p>
  </div>
  <div class="block body-text testimonials__col2">
    <div class="quote">
      <p>Carla is the kind of Real Estate professional everyone wants to represent them. She is knowledgeable, ethical, energetic, and follows up on every detail. Her honesty, integrity and expertise combined make her a very special and remarkable professional. We were lucky to find her!</p>
      <p class="sig">Martin &amp; Ellen Shaw</p>
    </div>
    <div class="quote">
      <p>Carla got us an amazing deal on our new home and sold our old home in a week. Carla is patient, hardworking, professional and most importantly HONEST. Carla is definitely one of the best in the business!</p>
      <p class="sig">Nina &amp; Owen Park</p>
    </div>
  </div>

  <div class="brokerage">
    <span class="brokerage__dot"></span>
    <span class="brokerage__name">Summit Realty</span>
  </div>

  <div class="contact">
    <p>Along with being your Realtor, I’m a lifelong resource for all things home-related &amp; beyond… if you need a great referral for anything at all, call me! I can’t wait to work with you!</p>
    <p class="contact__list">Carla Benedetti<br>555 201 4478<br>carla@carlabhomes.com<br>www.carlabhomes.com</p>
  </div>

  <div class="cover-logo">
    <span class="cover-logo__mark"></span>
    <span class="cover-logo__name">Carla Benedetti</span>
  </div>

  <p class="tagline">Helping people sell<br>and purchase homes<br>in Southern California</p>
</section>

<!-- Inner: two content pages -->
<section class="spread spread--inner">
  <svg class="spread__shapes" viewBox="0 0 560 409" aria-hidden="true">
    <polygon points="0,0 150,0 280,69 280,151 156,163 0,176" fill="var(--navy)"/>
    <polygon points="0,176 156,163 156,291 0,298" fill="var(--bright)"/>
    <polygon points="147,292 280,264 280,363" fill="var(--navy)"/>
    <polygon points="0,298 147,292 280,363 280,409 0,409" fill="var(--mist)"/>
    <polygon points="280,7 496,7 496,205 560,241 560,409 342,409 280,363" fill="var(--navy)"/>
    <polygon points="374,137 496,123 496,205" fill="var(--bright)"/>
  </svg>
  <div class="fold"></div>

  <div class="photo photo--portrait" role="img" aria-label="Portrait photo of the agent"></div>
  <div class="photo photo--estate" role="img" aria-label="Photo of a luxury home with pool at dusk"></div>
  <div class="photo photo--entrance" role="img" aria-label="Photo of a community entrance sign with fountains and palm trees"></div>

  <h2 class="block heading intro__title">Let me introduce myself</h2>
  <div class="block body-text intro__body">
    <p>I’m originally from Chicago, but I’m a full-fledged California girl now. I’ve lived and worked in Orange County since 1996. I always say where we live is the next best thing to living on a tropical island. I’ve traveled to many and I’m always happy to come back to my Laguna Niguel home.</p>
    <p>My passion for this area is why I’m in Real Estate. I consider myself incredibly fortunate to sell homes and help people purchase homes in an area that I love with all my heart.</p>
    <p>This passion also carries over in representing my clients with the highest degree of professionalism, enthusiasm and care. My business is built on exceptional customer service and I’m grateful my clients are mostly repeat and referrals.</p>
  </div>

  <h2 class="block heading tenet__title">My Core Tenet:<br>it’s all about YOU!</h2>
  <div class="block body-text tenet__body">
    <p>My #1 priority is understanding YOUR needs and YOUR objectives. This understanding, along with working diligently on your behalf, means we accomplish your goal whether you’re purchasing your 1st home or selling a home you’ve loved so you can move on to the next chapter of your life.</p>
  </div>

  <h2 class="block services__title serif">Real Estate Services &amp; Beyond…</h2>
  <div class="block body-text services__body">
    <p>Simply put, I help people who are local, relocating and investing, sell and purchase homes in Southern California. For purchases outside of California, I can refer to a network of agents across the country.</p>
    <p>I also provide a team who is dedicated to providing outstanding customer service throughout the transaction. My team includes a network of lenders, title, and escrow officers, in house CPA, stagers, photographers, contractors and more.</p>
  </div>

  <h2 class="block heading selling__title">Selling your home</h2>
  <div class="block body-text selling__body">
    <p>Selling your home is not like any other business transaction. It’s also personal. My priority as your Listing Agent is to guide you through what can be a complicated and sometimes emotional process.</p>
    <p>I place great emphasis on marketing your property with professional photographs, along with harnessing the power of the Internet and the virtual world to reach as many buyers as possible. Your property will be marketed to the public as well as to other agents, thus creating maximum exposure of your home.</p>
    <p>When we first meet to discuss selling your home, it’s essential for me to gain an understanding of your unique needs such as timelines, expectations and financial considerations, just to name a few. From there, I begin the process of listing and marketing your home. I lead you through negotiations and more paperwork than you ever care to do, guiding you to the successful closing of your home.</p>
  </div>

  <h2 class="block heading buying__title">Buying a home</h2>
  <div class="block body-text buying__body">
    <p>If you’re thinking about buying a home, it’s imperative you have an accomplished, real estate professional by your side to walk you through what is likely the largest purchase of your life.</p>
    <p>To get started, I like to meet with you so we have an opportunity to get to know each other as purchasing a home is a uniquely, personal endeavor. At that time, we can discuss your goals and if it’s a good time for you to purchase a home.</p>
    <p>From there, the first step is to obtain a pre-approval from a lender. I’m able to recommend various lenders who can introduce and explain the various loan products available.</p>
    <p>After you’ve been pre-approved, that’s when the fun starts! I guide you through the home buying adventure every step of the way and look forward to handing you the keys to your new home.</p>
  </div>
</section>

</body>
</html>
```